Business card design needed

Family General Practitioner/ Family Physician.
Logo is the logo of the Crestmoor Guild of Family Clinicians Australia
http://kvplm.tarevo.edu.au/PictureGallery/logos/pages/CGFC%20logo_jpg.htm

Reason: Just a bit more time to make changes and the weekend for me to look at things closely and to choose. Thanks, Lumi

Thanks for all the submissions. So many of them are really works of art. Not one of them are not good. The ones that I am eliminating are the ones that I think are not suitable for me personally only, and because if I don't, it makes it very difficult to decide as many of you are also sending me slight variations of a card. I have just decided to choose a second place card too. Can't thank you all enough. Good luck, Lumi. P.S - Working today till 10 pm as the card says :-), so probably won't be able to give a feedback till late Saturday night or Sunday morning here in Sydney, Australia. 

Reason: Just added a second place to the budget and realised that Australia is ahead of the rest of the world in the time zone (only :-) - don't want to offend anyone or start a debate!! ) , so Monday deadline will mean it will be a weekend for the rest of the world. Just wanted to give everyone more time to submit their best, especially since I will be picking a second card too. Can't thank everyone enough for the submissions. P.S - Not keen on photos on the card.

Contact Information for Business Card

Dr. Lumi Harcourt M.B.B.S., F.C.G.F.C
Family General Practitioner
Address, timings, phone and fax number on the back.

Requirements
Must have
• Timings
Mon 7 am - 7 pm
Tues 7 am - 12 pm
Wed 7 am - 10 pm
Thurs 7 am - 12 pm
Fri 7 am - 8 pm
Sat 8 am - 10 pm
Sun - Off

```html
<!DOCTYPE html>
<html lang="en">
<head>
<meta charset="utf-8">
<title>Dr. Lumi Harcourt – Business Card</title>
<link rel="stylesheet" href="https://fonts.googleapis.com/css2?family=Sorts+Mill+Goudy&display=swap">
<style>
  :root {
    --page-bg: #ffffff;
    --rule: #bfe0e4;
    --card-center: #0b7bc3;
    --card-mid: #0860a8;
    --card-edge: #283a86;
    --ink-light: #ffffff;
  }
  html, body {
    margin: 0;
    padding: 0;
    width: 1200px;
    height: 741px;
    overflow: hidden;
    background: var(--page-bg);
  }
  .canvas {
    position: relative;
    width: 1200px;
    height: 741px;
    font-family: "Sorts Mill Goudy", "Goudy Old Style", Georgia, serif;
  }
  .rule {
    position: absolute;
    left: 0;
    width: 1200px;
    height: 2px;
    background: var(--rule);
  }
  .rule--top { top: 6px; }
  .rule--bottom { top: 734px; }
  .card {
    position: absolute;
    left: 32px;
    top: 48px;
    width: 1133px;
    height: 646px;
    background: radial-gradient(ellipse 62% 68% at 47% 45%, var(--card-center) 0%, var(--card-mid) 55%, var(--card-edge) 100%);
    color: var(--ink-light);
  }
  .doctor-name {
    position: absolute;
    left: 60px;
    top: 192px;
    margin: 0;
    font-size: 68px;
    font-weight: 400;
    line-height: 1;
    white-space: nowrap;
  }
  .credentials {
    position: absolute;
    left: 61px;
    top: 305px;
    margin: 0;
    font-size: 32px;
    line-height: 1;
    letter-spacing: 0.5px;
    white-space: nowrap;
  }
  .role {
    position: absolute;
    left: 60px;
    top: 384px;
    margin: 0;
    font-size: 55px;
    font-weight: 400;
    line-height: 1;
    white-space: nowrap;
  }
  .guild-mark {
    position: absolute;
    left: 765px;
    top: 8px;
    width: 358px;
    height: 325px;
    display: flex;
    align-items: center;
    justify-content: center;
    gap: 16px;
  }
  .guild-mark__dot {
    width: 30px;
    height: 30px;
    border-radius: 50%;
    background: var(--ink-light);
  }
  .guild-mark__name {
    font-size: 58px;
    line-height: 1;
    color: var(--ink-light);
  }
</style>
</head>
<body>
  <div class="canvas">
    <div class="rule rule--top"></div>
    <section class="card">
      <h1 class="doctor-name">Dr. Lumi Harcourt</h1>
      <p class="credentials">M.B.B.S., F.C.G.F.C</p>
      <h2 class="role">Family General Practitioner</h2>
      <div class="guild-mark" aria-label="Crestmoor Guild of Family Clinicians Australia">
        <span class="guild-mark__dot"></span>
        <span class="guild-mark__name">CGFC</span>
      </div>
    </section>
    <div class="rule rule--bottom"></div>
  </div>
</body>
</html>
```